Pest control truck wrap

Needing an eye catching wrap for my new work truck. Its a 2018 Varenko Bellwick SR Access Cab with a Dunmar 240vkt canopy. It needs to stand out and be eye catching but not too busy, I want people to know who I am and what I'm doing. It also needs to be easily adaptable to my older trucks, which are full size without canopies. I prefer solid colors, probably black, white and green, and maybe a little orange. My logo should be large enough that it can be easily read from a distance, but not so big it takes up the whole truck. Since this is a pest control truck, it should communicate that. Bear in mind we primarily do insect and spider control, not rodents or wildlife. I'll include photos of the new truck, my logo, and one of my older trucks for reference.

```html
<!DOCTYPE html>
<html lang="en">
<head>
<meta charset="utf-8">
<title>Keystone Weed and Pest Control – Truck Wrap</title>
<link rel="stylesheet" href="https://fonts.googleapis.com/css2?family=Russo+One&display=swap">
<style>
  :root {
    --wrap-white: #f4f2ec;
    --wrap-black: #111111;
    --glass: #c9ced3;
    --stage: #ffffff;
    --line: #2a2a2a;
  }
  html, body {
    margin: 0;
    padding: 0;
    width: 1200px;
    height: 1200px;
    overflow: hidden;
    background: var(--stage);
  }
  .canvas {
    position: relative;
    width: 1200px;
    height: 1200px;
  }
  .wrap-layout {
    position: absolute;
    left: 0;
    width: 1200px;
    height: 469px;
  }
  .wrap-layout--canopy-left { top: 104px; }
  .wrap-layout--canopy-right { top: 621px; }
  .body-panel { fill: var(--wrap-white); stroke: var(--line); stroke-width: 2; }
  .black-field { fill: var(--wrap-black); }
  .white-stripe { fill: var(--wrap-white); }
  .window { fill: var(--glass); stroke: var(--wrap-black); stroke-width: 3; }
  .brand-circle { fill: none; stroke: var(--wrap-black); stroke-width: 7; }
  .brand-name, .tagline, .phone {
    font-family: "Russo One", sans-serif;
    fill: var(--wrap-black);
  }
  .spider-art { fill: #1c1c1c; }
</style>
</head>
<body>
<main class="canvas">

  <!-- Layout A: brand on doors, large artwork on canopy -->
  <svg class="wrap-layout wrap-layout--canopy-left" viewBox="0 0 960 375" role="group" aria-label="Wrap layout with artwork on canopy">
    <defs>
      <clipPath id="body-a">
        <path d="M40,265 L30,175 L50,160 L250,115 L300,55 Q305,45 320,45 L905,45 Q920,50 922,80 L928,250 L905,255 L850,255 A92,92 0 0 0 665,255 L245,265 A75,75 0 0 0 95,265 Z"/>
      </clipPath>
    </defs>
    <path class="body-panel" d="M40,265 L30,175 L50,160 L250,115 L300,55 Q305,45 320,45 L905,45 Q920,50 922,80 L928,250 L905,255 L850,255 A92,92 0 0 0 665,255 L245,265 A75,75 0 0 0 95,265 Z"/>
    <g clip-path="url(#body-a)">
      <path class="black-field" d="M720,40 L960,40 L960,300 L470,300 L560,255 L650,230 Z"/>
      <path class="white-stripe" d="M700,130 L960,115 L960,128 L705,142 Z"/>
      <rect class="spider-art" x="700" y="50" width="220" height="180" rx="30" role="img" aria-label="Large spider illustration across canopy"/>
      <path class="white-stripe" d="M470,300 L720,215 L730,222 L490,300 Z"/>
    </g>
    <rect class="window" x="355" y="65" width="95" height="55" rx="6"/>
    <rect class="window" x="472" y="65" width="70" height="55" rx="6"/>
    <rect class="window" x="580" y="62" width="140" height="52" rx="6"/>

    <circle class="brand-circle" cx="315" cy="203" r="52"/>
    <text class="tagline" x="455" y="140" font-size="14">Weed and Pest Control</text>
    <text class="brand-name" x="380" y="205" font-size="60" textLength="275" lengthAdjust="spacingAndGlyphs">Keystone</text>
    <text class="phone" x="396" y="240" font-size="22">(555) 014-2270</text>
  </svg>

  <!-- Layout B: black hood and roof sweep, brand across side, circle on canopy -->
  <svg class="wrap-layout wrap-layout--canopy-right" viewBox="0 0 960 375" role="group" aria-label="Wrap layout with black roof sweep">
    <defs>
      <clipPath id="body-b">
        <path d="M40,265 L30,175 L50,160 L250,115 L300,55 Q305,45 320,45 L905,45 Q920,50 922,80 L928,250 L905,255 L850,255 A92,92 0 0 0 665,255 L245,265 A75,75 0 0 0 95,265 Z"/>
      </clipPath>
    </defs>
    <path class="body-panel" d="M40,265 L30,175 L50,160 L250,115 L300,55 Q305,45 320,45 L905,45 Q920,50 922,80 L928,250 L905,255 L850,255 A92,92 0 0 0 665,255 L245,265 A75,75 0 0 0 95,265 Z"/>
    <g clip-path="url(#body-b)">
      <path class="black-field" d="M0,0 L960,0 L960,55 L700,72 L40,140 L0,145 Z"/>
      <path class="black-field" d="M45,160 L690,88 L692,96 L47,168 Z"/>
      <path class="black-field" d="M480,270 L960,185 L960,300 L480,300 Z"/>
      <path class="white-stripe" d="M560,275 L960,200 L960,208 L570,280 Z"/>
      <circle class="brand-circle" cx="783" cy="148" r="95"/>
    </g>
    <rect class="window" x="320" y="72" width="130" height="65" rx="6"/>
    <rect class="window" x="605" y="95" width="270" height="30" rx="6"/>

    <text class="tagline" x="90" y="184" font-size="14">Weed and Pest Control</text>
    <text class="brand-name" x="278" y="210" font-size="80" textLength="368" lengthAdjust="spacingAndGlyphs">Keystone</text>
    <text class="phone" x="385" y="246" font-size="22">(555) 014-2270</text>
  </svg>

</main>
</body>
</html>
```